Redesign of TaskHarbor.com website

Our website was initially developed 6+ years ago and has been maintained by several different designers. As a result, it is overly complex, inconsistent format/layout and the content is not well structured/easy to navigate

We need the site redeveloped with a more modern look and feel, simpler content structure and ability to implement new/improved tools, such as: Dynamic Forms, Sales Funnels, Landing Pages, improved metadata of our pages and posts, improved SEO/Page ranking, etc.

We currently use DealRiver CRM, Steady Reach for marketing automation and GridPilot forms. We are investigating Floxen for workflow integration which could extend to our website.

Our current website is developed in WordPress, ideally we will stick with this platform, but we’re happy to consider other CMS' if strongly recommended. We may decide to remove/consolidate some of the pages and/or content as part of this re-design.

We don't want to rebrand (ie change corporate logo, colours scheme etc) as part of this website redevelopment and it is critical that we don't lose our current Page Ranking, SEO rankings, backlink benefits, etc as part of this redevelopment.

Sites we like the feel/design of are: boardwiley.com, tallypoint.com and rankgrove.com

Target Market(s)

Corporate, Enterprise and Government B2B clients.

Coding

Coded - Design and coding required

Number of Pages Required

5+ page

Font styles to use
Sans Serif

Colors
ffffff
ec1f27

Requirements
Must have
• Must retain the majority of content on our existing website (although we may re-write some of it as part of this redesign process).
Nice to have
• See above "Project Description"
Should not have

```html
<!DOCTYPE html>
<html lang="en">
<head>
<meta charset="utf-8">
<title>TaskHarbor – Your Trusted Advisor</title>
<link rel="stylesheet" href="https://fonts.googleapis.com/css2?family=Montserrat:wght@500;600;700&family=Roboto:wght@400;500;700&display=swap">
<style>
:root{
  --red:#e0141d;
  --white:#ffffff;
  --ink:#111111;
  --text:#222222;
  --muted:#666666;
  --blush:#fdf0f1;
  --footer:#000000;
  --card-shadow:0 2px 10px rgba(0,0,0,.12);
}
*{box-sizing:border-box;margin:0;padding:0}
html,body{width:1200px;height:3509px;overflow:hidden}
body{position:relative;background:var(--white);font-family:"Roboto",Arial,sans-serif;color:var(--text)}
.abs{position:absolute}
.top-bar{left:0;top:0;width:1200px;height:8px;background:var(--red)}
.brand{display:flex;align-items:center;gap:10px}
.brand-dot{width:22px;height:22px;border-radius:50%;background:var(--red);flex:none}
.brand-name{font-family:"Roboto",sans-serif;font-weight:700;font-size:24px;line-height:1;color:var(--ink)}
.header-brand{left:86px;top:42px}
.main-nav{left:329px;top:48px;font-family:"Roboto",sans-serif;font-weight:500;font-size:15px}
.main-nav a{text-decoration:none;color:var(--ink);position:absolute;white-space:nowrap}
.main-nav a.active{color:var(--red)}
.search-icon{left:1096px;top:49px}
.hero{left:0;top:104px;width:1200px;height:630px;overflow:hidden}
.hero-photo{position:absolute;inset:0;background:linear-gradient(180deg,#8fa3b5 0%,#b7a08a 45%,#6d6656 70%,#3f4440 100%)}
.hero-curve{position:absolute;left:0;top:0}
.hero-title{left:85px;top:262px;font-family:"Montserrat",sans-serif;font-weight:700;font-size:43px;line-height:44px;color:var(--white)}
.hero-text{left:85px;top:368px;width:460px;font-size:15px;line-height:26px;color:var(--white)}
.btn{display:inline-block;background:var(--red);color:var(--white);font-family:"Roboto",sans-serif;font-weight:700;font-size:15px;text-decoration:none}
.hero-btn{left:85px;top:444px;width:118px;height:38px;line-height:38px;text-align:center}
.dots{left:578px;top:641px;display:flex;gap:9px}
.dots span{width:9px;height:9px;border-radius:50%;background:var(--white)}
.dots span.on{background:var(--red)}
.section-title{width:1200px;left:0;text-align:center;font-family:"Montserrat",sans-serif;font-weight:700;font-size:38px;color:var(--ink)}
.rule{width:48px;height:3px;background:var(--red);left:576px}
.service-card{top:919px;width:226px;height:241px;background:var(--white);box-shadow:var(--card-shadow);display:flex;flex-direction:column;align-items:center;justify-content:center;text-align:center;font-size:15px;line-height:25px;color:var(--ink);text-transform:uppercase}
.service-card svg{margin-bottom:14px}
.service-card.featured{background:var(--red);color:var(--white)}
.about-panel{left:0;top:1246px;width:602px;height:502px;background:linear-gradient(135deg,#d3141d,#e92930 60%,#d0121b)}
.about-photo{left:602px;top:1246px;width:598px;height:502px;background:linear-gradient(120deg,#c7ccd1 0%,#9aa0a6 45%,#4a4f56 100%)}
.about-title{left:77px;top:1335px;font-family:"Montserrat",sans-serif;font-weight:700;font-size:38px;color:var(--white)}
.about-rule{left:77px;top:1399px;width:48px;height:3px;background:var(--white)}
.about-text{left:77px;top:1442px;width:470px;font-size:15px;line-height:26px;color:var(--white)}
.outline-btn{left:77px;top:1608px;width:121px;height:42px;line-height:40px;text-align:center;border:1px solid var(--white);color:var(--white);font-weight:700;font-size:15px}
.news-card{background:var(--white);box-shadow:var(--card-shadow)}
.ph{background:linear-gradient(135deg,#b9bdc0,#6f7579)}
.news-title{font-family:"Roboto",sans-serif;font-weight:500;font-size:15.5px;line-height:26px;color:var(--ink)}
.news-title.big{font-size:17px}
.news-cat{font-size:14px;color:var(--red)}
.news-text{font-size:14.5px;line-height:26px;color:var(--ink)}
.news-btn{text-align:center}
.testimonials{left:0;top:2488px;width:1200px;height:700px;background:var(--blush)}
.quote{width:276px;text-align:center;font-size:14.5px;line-height:26px;color:var(--ink)}
.quote-mark{font-family:"Montserrat",sans-serif;font-weight:700;font-size:160px;line-height:1;color:rgba(224,20,29,.12)}
.quote-box{left:427px;top:2726px;width:347px;height:166px;border:1.5px solid var(--red);display:flex;align-items:center;justify-content:center}
.avatar{width:56px;height:56px;border-radius:50%;background:linear-gradient(180deg,#d9dcdf,#55606b)}
.person{width:276px;text-align:center;font-weight:700;font-size:15px;color:var(--ink)}
.footer{left:0;top:3040px;width:1200px;height:469px;background:var(--footer)}
.footer-curve{position:absolute;left:0;top:0}
.footer-brand{left:0;width:1200px;top:3158px;justify-content:center}
.footer-brand .brand-name{font-size:34px;color:var(--white)}
.footer-brand .brand-dot{width:28px;height:28px}
.footer-nav{top:3242px;font-weight:700;font-size:15px;color:var(--white)}
.footer-nav span{position:absolute;white-space:nowrap}
.contact{display:flex;align-items:center;gap:14px;color:var(--white);font-size:15px;line-height:25px}
.contact-icon{width:34px;height:34px;border-radius:50%;background:var(--red);display:flex;align-items:center;justify-content:center;flex:none}
.footer-line{left:85px;top:3410px;width:1030px;height:1px;background:#444}
.copyright{left:0;width:1200px;top:3447px;text-align:center;color:var(--white);font-size:14.5px}
</style>
</head>
<body>
<div class="abs top-bar"></div>

<header>
  <div class="abs brand header-brand">
    <span class="brand-dot"></span>
    <span class="brand-name">TaskHarbor</span>
  </div>
  <nav class="abs main-nav">
    <a class="active" style="left:0">HOME</a>
    <a style="left:90px">SERVICES</a>
    <a style="left:206px">ABOUT</a>
    <a style="left:304px">CLIENTS</a>
    <a style="left:412px">RESOURCES</a>
    <a style="left:548px">BLOG</a>
    <a style="left:635px">CONTACT</a>
  </nav>
  <svg class="abs search-icon" width="14" height="14" viewBox="0 0 14 14"><circle cx="6" cy="6" r="4.5" fill="none" stroke="#111" stroke-width="2"/><line x1="9.3" y1="9.3" x2="13" y2="13" stroke="#111" stroke-width="2"/></svg>
</header>

<section class="abs hero">
  <div class="hero-photo" role="img" aria-label="City skyline photograph with river and bridge at sunset"></div>
  <svg class="hero-curve" width="1200" height="630" viewBox="0 0 1200 630">
    <path d="M0 512 Q560 700 1200 536 L1200 630 L0 630 Z" fill="#e0141d"/>
    <path d="M0 522 Q560 716 1200 546 L1200 630 L0 630 Z" fill="#ffffff"/>
  </svg>
</section>
<h1 class="abs hero-title">TASKHARBOR YOUR<br>TRUSTED ADVISOR</h1>
<p class="abs hero-text">TaskHarbor provides an ongoing management and maintenance service to ensure that plan documentation is always current.</p>
<a class="abs btn hero-btn">GET STARTED</a>
<div class="abs dots"><span class="on"></span><span></span><span></span></div>

<h2 class="abs section-title" style="top:796px">OUR SERVICES</h2>
<div class="abs rule" style="top:854px"></div>

<div class="abs service-card" style="left:85px">
  <svg width="90" height="90" viewBox="0 0 90 90" fill="none" stroke="#e0141d" stroke-width="6"><circle cx="45" cy="45" r="40"/><path d="M24 50c4-12 14-12 21-5s17 7 21-5" stroke-linecap="round"/><path d="M24 40c4 12 14 12 21 5" stroke-linecap="round"/></svg>
  <span>Resilience &amp;<br>Continuity</span>
</div>
<div class="abs service-card" style="left:351px">
  <svg width="86" height="96" viewBox="0 0 86 96" fill="none" stroke="#e0141d" stroke-width="4"><path d="M43 4 L80 16 V46 C80 70 62 84 43 92 C24 84 6 70 6 46 V16 Z"/><path d="M22 46 C22 30 64 30 64 46 Z" stroke-linejoin="round"/><path d="M43 46 V64 C43 70 35 70 35 64"/></svg>
  <span>Security<br>Management</span>
</div>
<div class="abs service-card featured" style="left:618px">
  <svg width="80" height="92" viewBox="0 0 80 92" fill="none" stroke="#ffffff" stroke-width="3.5"><circle cx="36" cy="20" r="14"/><path d="M12 62 C12 44 60 44 60 62"/><rect x="8" y="60" width="48" height="28" rx="3"/><circle cx="60" cy="50" r="14" fill="#e0141d"/><path d="M54 56 L66 44"/></svg>
  <span>IT Services &amp;<br>Solutions</span>
</div>
<div class="abs service-card" style="left:884px">
  <svg width="94" height="84" viewBox="0 0 94 84" fill="none" stroke="#e0141d" stroke-width="4"><rect x="12" y="22" width="68" height="46" rx="3"/><path d="M2 74 H92"/><circle cx="42" cy="44" r="10"/><circle cx="66" cy="18" r="8"/><path d="M42 30 V34 M42 54 V58 M28 44 H32 M52 44 H56"/></svg>
  <span>Data Management</span>
</div>

<div class="abs about-panel" role="img" aria-label="Red-tinted photograph of business colleagues in a meeting"></div>
<div class="abs about-photo" role="img" aria-label="Photograph of three colleagues discussing work at a laptop"></div>
<h2 class="abs about-title">ABOUT US</h2>
<div class="abs about-rule"></div>
<p class="abs about-text">As an executive in any business, it is understandable that you want to ensure it is 100% safe, because your business is only as strong as its weakest link.You know that if you have a disastrous incident it will cause irreversible damage to your company's good name, your shareholders, board of directors and industry regulators.</p>
<a class="abs outline-btn">LEARN MORE</a>

<h2 class="abs section-title" style="top:1824px">OUR NEWS</h2>
<div class="abs rule" style="top:1891px"></div>

<article class="abs news-card" style="left:83px;top:1938px;width:409px;height:464px"></article>
<div class="abs ph" style="left:92px;top:1948px;width:390px;height:170px" role="img" aria-label="Photograph of hands being washed under a tap"></div>
<h3 class="abs news-title big" style="left:92px;top:2140px">COVID19 – Business Recovery Phase</h3>
<p class="abs news-cat" style="left:92px;top:2190px">Business Continuity, Pandemic</p>
<p class="abs news-text" style="left:92px;top:2230px;width:380px">The following is a summary of the status updates and actions in preparing for the Recovery Phase and addressing new risks which have been identified.</p>
<a class="abs btn news-btn" style="left:92px;top:2334px;width:148px;height:40px;line-height:40px;font-size:16px">LEARN MORE</a>

<article class="abs news-card" style="left:508px;top:1938px;width:609px;height:220px"></article>
<div class="abs ph" style="left:523px;top:1948px;width:239px;height:204px;background:linear-gradient(135deg,#e9dfcf,#c9b89a)" role="img" aria-label="Photograph of a hand writing on paper beside a keyboard"></div>
<h3 class="abs news-title" style="left:793px;top:1950px;width:310px">Adapt or Die – A Darwinian Take on Business Continuity</h3>
<p class="abs news-cat" style="left:793px;top:2014px">Business Continuity</p>
<p class="abs news-text" style="left:793px;top:2044px;width:310px">Most businesses experience change constantly. Markets,technologies,regulations</p>
<a class="abs btn news-btn" style="left:793px;top:2108px;width:131px;height:32px;line-height:32px;font-size:14.5px">LEARN MORE</a>

<article class="abs news-card" style="left:508px;top:2180px;width:609px;height:220px"></article>
<div class="abs ph" style="left:523px;top:2188px;width:239px;height:204px;background:linear-gradient(135deg,#cfd6dc,#4a5866)" role="img" aria-label="Photograph of a person using a tablet with data graphics"></div>
<h3 class="abs news-title" style="left:793px;top:2190px;width:310px">How's Your User Experience for Your Disaster Recovery?</h3>
<p class="abs news-cat" style="left:793px;top:2254px">Disaster Recovery</p>
<p class="abs news-text" style="left:793px;top:2284px;width:310px">It may sound strange to talk about "touchy-feely" stuff like user experience</p>
<a class="abs btn news-btn" style="left:793px;top:2348px;width:131px;height:32px;line-height:32px;font-size:14.5px">LEARN MORE</a>

<section class="abs testimonials"></section>
<h2 class="abs section-title" style="top:2543px">OUR TESTIMONIALS</h2>
<div class="abs rule" style="top:2606px"></div>

<div class="abs quote-mark" style="left:178px;top:2660px">“</div>
<p class="abs quote" style="left:88px;top:2712px">"It was good to work with you.&amp;nbsp; There are very few true professional organisations such as yours, in this industry.&amp;nbsp;&amp;nbsp;"</p>
<div class="abs avatar" style="left:198px;top:2836px" role="img" aria-label="Portrait of the reviewer"></div>
<p class="abs person" style="left:88px;top:2914px">Northvale Systems</p>

<div class="abs quote-box"><p class="quote" style="width:290px">"The knowledge you've amassed about our IT environment in such as short space of time is incredible.&amp;nbsp; We have been trying to develop this same</p></div>
<div class="abs avatar" style="left:572px;top:2920px" role="img" aria-label="Portrait of Leon Marsh"></div>
<p class="abs person" style="left:462px;top:2997px">Leon Marsh</p>

<div class="abs quote-mark" style="left:925px;top:2660px">“</div>
<p class="abs quote" style="left:836px;top:2712px">"With all due respect, I don't see TaskHarbor in the classic consultant mould.&amp;nbsp; I see you far more as 'hands-on implementation practitioners',</p>
<div class="abs avatar" style="left:945px;top:2836px" role="img" aria-label="Portrait of Adrian Vell"></div>
<p class="abs person" style="left:836px;top:2914px">Adrian Vell</p>

<footer class="abs footer">
  <svg class="footer-curve" width="1200" height="110" viewBox="0 0 1200 110">
    <rect width="1200" height="110" fill="#fdf0f1"/>
    <path d="M0 102 Q600 -20 1200 92 L1200 110 L0 110 Z" fill="#e0141d"/>
    <path d="M0 106 Q620 0 1200 100 L1200 110 L0 110 Z" fill="#000000"/>
  </svg>
</footer>
<div class="abs brand footer-brand">
  <span class="brand-dot"></span>
  <span class="brand-name">TaskHarbor</span>
</div>
<div class="abs footer-nav" style="left:0">
  <span style="left:255px">HOME</span>
  <span style="left:342px">SERVICES</span>
  <span style="left:454px">ABOUT</span>
  <span style="left:548px">CLIENTS</span>
  <span style="left:657px">RESOURCES</span>
  <span style="left:789px">BLOG</span>
  <span style="left:871px">CONTACT</span>
</div>

<div class="abs contact" style="left:210px;top:3323px">
  <span class="contact-icon"><svg width="16" height="16" viewBox="0 0 16 16"><path d="M3 1 L6 1 L7 5 L5 6.5 C6 9 7 10 9.5 11 L11 9 L15 10 V13 C15 14 14 15 13 15 C6 15 1 10 1 3 C1 2 2 1 3 1 Z" fill="#fff"/></svg></span>
  <span>612 9000 4821</span>
</div>
<div class="abs contact" style="left:453px;top:3310px">
  <span class="contact-icon"><svg width="14" height="18" viewBox="0 0 14 18"><path d="M7 1 C3.5 1 1 3.5 1 7 C1 11 7 17 7 17 C7 17 13 11 13 7 C13 3.5 10.5 1 7 1 Z" fill="#fff"/><circle cx="7" cy="7" r="2.3" fill="#e0141d"/></svg></span>
  <span>PO Box 4410 Sydney&nbsp; NSW&nbsp; 2001<br>Australia</span>
</div>
<div class="abs contact" style="left:801px;top:3323px">
  <span class="contact-icon"><svg width="16" height="12" viewBox="0 0 16 12" fill="none" stroke="#fff" stroke-width="1.6"><rect x="1" y="1" width="14" height="10" rx="1.5"/><path d="M1 2 L8 7 L15 2"/></svg></span>
  <span>info@taskharbor.com</span>
</div>
<div class="abs footer-line"></div>
<p class="abs copyright">©Copyrights 2021 TaskHarbor Your Trusted advisor.All right Reserved.</p>
</body>
</html>
```